Kestrel Aid Services Banner Ad

Need a 750 x 250-pixel banner ad with the company Logo included. Please see company website at www.kestrelaidservices.com for more information.

```html
<!DOCTYPE html>
<html lang="en">
<head>
<meta charset="utf-8">
<title>Kestrel Aid Services Banner</title>
<link rel="stylesheet" href="https://fonts.googleapis.com/css2?family=Poppins:wght@400;600&display=swap">
<style>
  :root {
    --white: #ffffff;
    --green: #7dc242;
    --navy: #0d3a63;
    --navy-deep: #0c2356;
    --grey-band: #d6d6d6;
    --grey-line: #b9bcc2;
    --text: #4a4a4a;
    --photo-a: #7c8f4a;
    --photo-b: #c79a80;
    --photo-c: #3f5a2a;
  }
  html, body {
    margin: 0;
    padding: 0;
    overflow: hidden;
    background: var(--white);
  }
  .banner {
    position: relative;
    width: 1200px;
    height: 400px;
    overflow: hidden;
    background: var(--white);
    font-family: "Poppins", Arial, sans-serif;
  }
  .shapes {
    position: absolute;
    inset: 0;
  }
  .brand {
    position: absolute;
    left: 173px;
    top: 100px;
    display: flex;
    align-items: center;
    gap: 16px;
  }
  .brand-mark {
    width: 52px;
    height: 52px;
    border-radius: 50%;
    background: var(--navy);
  }
  .brand-name {
    font-weight: 600;
    font-size: 31px;
    color: var(--green);
    letter-spacing: 0.3px;
    white-space: nowrap;
  }
  .tagline {
    position: absolute;
    right: 605px;
    top: 215px;
    margin: 0;
    text-align: right;
    font-weight: 400;
    font-size: 20px;
    line-height: 40px;
    color: var(--text);
  }
</style>
</head>
<body>
<div class="banner">
  <svg class="shapes" width="1200" height="400" viewBox="0 0 1200 400" aria-hidden="false">
    <defs>
      <linearGradient id="photo-tones" x1="0" y1="0" x2="1" y2="1">
        <stop offset="0" stop-color="var(--photo-a)"/>
        <stop offset="0.5" stop-color="var(--photo-b)"/>
        <stop offset="1" stop-color="var(--photo-c)"/>
      </linearGradient>
    </defs>
    <polygon class="corner-accent" points="0,0 61,0 112,99 0,99" fill="var(--green)"/>
    <polygon class="grey-band" points="509,0 572,0 812,400 752,400" fill="var(--grey-band)"/>
    <polygon class="photo" role="img" aria-label="Photo of a smiling young woman carrying a happy little girl on her back outdoors"
             points="566,0 1200,0 1200,400 806,400" fill="url(#photo-tones)"/>
    <polygon class="corner-line" points="1004,0 1020,0 1200,288 1200,314" fill="var(--grey-line)"/>
    <polygon class="corner-navy" points="1024,0 1200,0 1200,280" fill="var(--navy-deep)"/>
    <polygon class="base-block" points="344,328 592,328 634,400 384,400" fill="var(--navy)"/>
  </svg>

  <div class="brand">
    <span class="brand-mark"></span>
    <span class="brand-name">Kestrel Aid Services</span>
  </div>

  <p class="tagline">Positive difference in the lives to the individuals we<br>serve through Support Coordination.</p>
</div>
</body>
</html>
```